Personal sales brochure for client marketing

I am looking for a brochure in the style of a sales menu to sit in front of clients with. I want 5 different colored columns where clients will choose the right package for them.
Eg.
Package 1 called Book-keeping is a basic package
Package 2 called Insight includes the above but also extra services
Package 3 called Compliance an add on for the above packages
Package 4 Called Professional another add on to the above services
Package 5 called payroll another add on to the above.

I want to sit in front of my clients and discuss the services we provide and allow them to choose from this list and tick the boxes of what they would like. I attach a simple spread sheet as well for guideline.

Target Market(s)

business owners requiring accounting support and advice

Industry/Entity Type

Accounting

Font styles to use
Serif
Sans Serif

Requirements
Must have
• Simple, clear, concise with clear product descriptions in colored boxes that highlight clearly the different options. Must have Logo and contact details. This document need to be our key sales and marketing tool so will need to introduce the business clearly and in a professional manner.
• enquiries@brantwellpartners.gg
• 01481 439216
Nice to have
• The design needs to be printable on A1 A3 A4 A5
Should not have
• Pictures and patterns

```html
<!DOCTYPE html>
<html lang="en">
<head>
<meta charset="utf-8">
<title>Brantwell Partners – Special Packages</title>
<link href="https://fonts.googleapis.com/css2?family=Arimo:wght@400;700&family=Cormorant+Garamond:ital,wght@0,500;1,500&family=Gelasio:wght@400&family=Oswald:wght@700&display=swap" rel="stylesheet">
<style>
  :root{
    --ink:#1a1a1a;
    --muted:#333;
    --paper:#ffffff;
    --p1-bg:#f7cbcb; --p1-num:#ee8e8e;
    --p2-bg:#ffffcf; --p2-num:#f6f27c;
    --p3-bg:#dbf6d0; --p3-num:#a9ef8c;
    --p4-bg:#cbfbfb; --p4-num:#8cf2f2;
    --p5-bg:#fbcdf8; --p5-num:#f48ff0;
  }
  *{box-sizing:border-box;margin:0;padding:0}
  html,body{width:1200px;height:848px;overflow:hidden;background:var(--paper)}
  .sheet{position:relative;width:1200px;height:848px;background:var(--paper);color:var(--ink);font-family:"Arimo",Arial,sans-serif}

  .brand{position:absolute;top:38px;left:0;width:100%;text-align:center}
  .brand-name{font-family:"Gelasio",Georgia,serif;font-size:30px;letter-spacing:3px;color:var(--ink);line-height:1}
  .brand-tag{font-size:9px;letter-spacing:2px;color:var(--ink);margin-top:5px}

  .title{position:absolute;top:108px;left:0;width:100%;text-align:center;font-family:"Cormorant Garamond",Georgia,serif;font-weight:500;font-size:50px;letter-spacing:9px;line-height:1}
  .title-rule{position:absolute;top:176px;left:427px;width:344px;height:2px;background:var(--ink)}

  .intro{position:absolute;top:203px;left:0;width:100%;text-align:center;font-size:17px;line-height:25px;letter-spacing:.6px}

  .packages{position:absolute;top:280px;left:23px;display:flex;gap:29px}
  .package{position:relative;width:207px;height:440px;border-radius:12px;overflow:hidden;padding:14px 16px 0}
  .package--1{background:var(--p1-bg);--num:var(--p1-num)}
  .package--2{background:var(--p2-bg);--num:var(--p2-num)}
  .package--3{background:var(--p3-bg);--num:var(--p3-num)}
  .package--4{background:var(--p4-bg);--num:var(--p4-num)}
  .package--5{background:var(--p5-bg);--num:var(--p5-num)}
  .package-num{position:absolute;right:20px;bottom:-40px;font-family:"Oswald",Impact,sans-serif;font-weight:700;font-size:330px;line-height:1;color:var(--num);z-index:0}
  .package>*:not(.package-num){position:relative;z-index:1}
  .package-title{font-family:"Gelasio",Georgia,serif;font-weight:400;font-size:20px;line-height:28px;letter-spacing:.5px;text-transform:uppercase;height:76px}

  .options{list-style:none;margin-bottom:14px}
  .options li{display:flex;align-items:center;font-size:15px;height:27px}
  .box{width:14px;height:14px;border:2px solid var(--ink);margin-right:12px;flex:none}

  .services{list-style:none}
  .services li{position:relative;padding-left:10px;font-size:10.5px;line-height:12px;margin-bottom:14px;text-align:justify}
  .services li::before{content:"";position:absolute;left:0;top:4px;width:3px;height:3px;border-radius:50%;background:var(--ink)}

  .note{position:absolute;font-family:"Cormorant Garamond",Georgia,serif;font-style:italic;font-weight:500;font-size:15.5px;color:var(--ink);letter-spacing:.3px}
  .note--a{top:744px;left:98px}
  .note--b{top:770px;left:437px}

  .contact{position:absolute;top:808px;left:0;width:100%;text-align:center;font-size:17px;letter-spacing:.8px;color:var(--muted)}
  .contact .sep{margin:0 12px}
</style>
</head>
<body>
<main class="sheet">
  <header class="brand">
    <div class="brand-name">BRANTWELL PARTNERS</div>
    <div class="brand-tag">ACCOUNTING &amp; BUSINESS SOLUTIONS</div>
  </header>

  <h1 class="title">SPECIAL PACKAGES</h1>
  <div class="title-rule"></div>

  <p class="intro">EVERY BUSINESS IS DIFFERENT<br>WHEN WE UNDERSTAND YOUR NEEDS, WE CAN PROVIDE JUST THE SERVICES YOU REQUIRE AT AN AGREED FEE.</p>

  <section class="packages">
    <article class="package package--1">
      <span class="package-num" aria-hidden="true">1</span>
      <h2 class="package-title">Package 1 :<br>Book-keeping</h2>
      <ul class="options"><li><span class="box"></span>Monthly</li><li><span class="box"></span>Quarterly</li><li><span class="box"></span>Annually</li></ul>
      <ul class="services">
        <li>Invoices entered</li>
        <li>Bank accounts reconciled</li>
        <li>Purchase reconciled</li>
        <li>Sales ledgers reconciled</li>
      </ul>
    </article>

    <article class="package package--2">
      <span class="package-num" aria-hidden="true">2</span>
      <h2 class="package-title">Package 2 :<br>Insight</h2>
      <ul class="options"><li><span class="box"></span>Monthly</li><li><span class="box"></span>Quarterly</li><li><span class="box"></span>Annually</li></ul>
      <ul class="services">
        <li>All services in Package 1</li>
        <li>Accounting adjustments - a true reflection for your profit / loss to date</li>
        <li>Management accounts</li>
        <li>Regular meeting to discuss business performance and possible areas for improvement</li>
        <li>All software is included</li>
        <li>Unlimited support and assistance</li>
      </ul>
    </article>

    <article class="package package--3">
      <span class="package-num" aria-hidden="true">3</span>
      <h2 class="package-title">Package 3 :<br>Compliance</h2>
      <ul class="options"><li><span class="box"></span>Monthly</li><li><span class="box"></span>Quarterly</li><li><span class="box"></span>Annually</li></ul>
      <ul class="services">
        <li>All services in Package 1 &amp; 2</li>
        <li>Financial statements prepared</li>
        <li>Income tax computation</li>
        <li>Personal tax returns</li>
        <li>All software is included</li>
        <li>Unlimited support and assistance</li>
      </ul>
    </article>

    <article class="package package--4">
      <span class="package-num" aria-hidden="true">4</span>
      <h2 class="package-title">Package 4 :<br>Professional</h2>
      <ul class="options"><li><span class="box"></span>Monthly</li><li><span class="box"></span>Quarterly</li><li><span class="box"></span>Annually</li></ul>
      <ul class="services">
        <li>All services in Package 1 &amp; 2 &amp; 3</li>
        <li>Bespoke solutions for your business</li>
        <li>Business planning</li>
        <li>Cash flow planning and fore-casting</li>
        <li>Specialist tax planning</li>
        <li>Business turnaround</li>
        <li>All software is included</li>
        <li>Unlimited support and assistance</li>
      </ul>
    </article>

    <article class="package package--5">
      <span class="package-num" aria-hidden="true">5</span>
      <h2 class="package-title">Package 5 :<br>Payroll</h2>
      <ul class="options"><li><span class="box"></span>Weekly</li><li><span class="box"></span>Monthly</li></ul>
      <ul class="services" style="margin-top:27px">
        <li>Additional service</li>
        <li>ETI Returns</li>
        <li>UK / Channel Island</li>
      </ul>
    </article>
  </section>

  <p class="note note--a">Many clients have a need for a “catch-up” project to get their books and accounts up to date.</p>
  <p class="note note--b">We will agree with you a plan to complete the project at the outset and agree a fixed price.</p>

  <footer class="contact">www.brantwellpartners.gg<span class="sep">|</span>enquiries@brantwellpartners.gg<span class="sep">|</span>01481 439216</footer>
</main>
</body>
</html>
```